Health Information/Education Logo Design

We need a logo design for a new company based in Atlanta called Meadowlark Health. The program is about patient empowerment. We provide health information and education on how to get healthy, stay healthy, and how to be proactive in your care. We also provide medication and injection training to help patients feel their best and to ensure successful therapy outcomes.
We like the colors yellow, pink, teal and purple and would like to see some or all of these colors in the designs. The final design should communicate caring, considerate, compassionate information, education and training services
Industry/Entity Type
Education
Contact Information for Business Card
Meadowlark Health
Danielle Ostrander RN, MSN, MHA
Nurse Educator
555.214.3096 cell
555.470.2283 fax

```html
<!DOCTYPE html>
<html lang="en">
<head>
<meta charset="utf-8">
<title>Meadowlark Health – Business Card</title>
<link href="https://fonts.googleapis.com/css2?family=Questrial&display=swap" rel="stylesheet">
<style>
  :root {
    --bg: #d9dadc;
    --card-white: #ffffff;
    --teal: #19b3b8;
    --teal-deep: #14999f;
    --yellow: #f2ea1c;
    --ink-light: #ffffff;
    --grey-text: #9a9a9a;
  }
  html, body {
    margin: 0;
    width: 1200px;
    height: 1000px;
    overflow: hidden;
    background: var(--bg);
  }
  .canvas {
    position: relative;
    width: 1200px;
    height: 1000px;
    font-family: "Questrial", sans-serif;
  }
  .business-card {
    position: absolute;
    left: 75px;
    top: 200px;
    width: 1050px;
    height: 600px;
    border-radius: 34px;
    overflow: hidden;
    background: var(--card-white);
    box-shadow: 0 12px 30px rgba(0,0,0,0.18);
  }
  .card-shapes {
    position: absolute;
    inset: 0;
  }
  .brand {
    position: absolute;
    left: 70px;
    top: 250px;
    display: flex;
    align-items: center;
    gap: 18px;
  }
  .brand-dot {
    width: 30px;
    height: 30px;
    border-radius: 50%;
    background: var(--yellow);
  }
  .brand-name {
    font-size: 42px;
    color: var(--teal);
    letter-spacing: 0.5px;
    white-space: nowrap;
  }
  .contact {
    position: absolute;
    left: 640px;
    top: 205px;
    color: var(--ink-light);
  }
  .contact-name {
    font-size: 42px;
    margin: 0;
    font-weight: 400;
    letter-spacing: 0.3px;
  }
  .contact-title {
    font-size: 23px;
    margin: 8px 0 0 4px;
    opacity: 0.95;
  }
  .contact-phones {
    display: flex;
    align-items: center;
    gap: 8px;
    font-size: 25px;
    margin: 34px 0 0 4px;
  }
  .icon {
    width: 16px;
    height: 24px;
    flex: none;
  }
</style>
</head>
<body>
<div class="canvas">
  <div class="business-card">
    <svg class="card-shapes" width="1050" height="600" viewBox="0 0 1050 600" aria-hidden="true">
      <defs>
        <linearGradient id="tealPanel" x1="0" y1="0" x2="1" y2="1">
          <stop offset="0" stop-color="var(--teal-deep)"/>
          <stop offset="1" stop-color="var(--teal)"/>
        </linearGradient>
      </defs>
      <path d="M520 0 Q650 300 545 600 L1050 600 L1050 0 Z" fill="url(#tealPanel)"/>
      <path d="M506 0 Q636 300 531 600" fill="none" stroke="var(--yellow)" stroke-width="10"/>
    </svg>

    <div class="brand">
      <span class="brand-dot"></span>
      <span class="brand-name">Meadowlark Health</span>
    </div>

    <div class="contact">
      <h1 class="contact-name">Danielle Ostrander</h1>
      <p class="contact-title">RN, MSN, MHA Nurse Educator</p>
      <div class="contact-phones">
        <svg class="icon" viewBox="0 0 16 24" aria-label="cell">
          <rect x="2" y="1" width="12" height="22" rx="2" fill="none" stroke="var(--yellow)" stroke-width="2"/>
          <line x1="6" y1="19" x2="10" y2="19" stroke="var(--yellow)" stroke-width="2"/>
        </svg>
        <span>555.214.3096 | 555.470.2283</span>
        <svg class="icon" viewBox="0 0 16 24" aria-label="fax">
          <rect x="1" y="9" width="14" height="12" rx="1.5" fill="none" stroke="var(--yellow)" stroke-width="2"/>
          <rect x="4" y="3" width="8" height="6" fill="none" stroke="var(--yellow)" stroke-width="2"/>
        </svg>
      </div>
    </div>
  </div>
</div>
</body>
</html>
```